Mortgage Loan officer needs clean/modern business card design

Looking for a clean, modern 2-sided business card design. We like the earth tones used in our logo and website http://vukarhome-lending.example . Would also like to incorporate: 1) Something special to make our card stand out - a pop of color or embossed logo, for instance and 2) please include "Mortgage Loans" "Reverse Mortgages" "Private Money Loans" on back of card with the logo.

Front: Needs to include agent/company license info - see website. Agent name: Niall Hargrove

Here are fonts and colors used for our logo:
Font: Avenir Next
Colors:
#2c3539 - Dark Gray
#576870 - Light Gray
#ffffff - Background White

Target Market(s)

Prospects and current clients. Will also be distributing to people in professional network (attorneys and CPAs)

Industry/Entity Type

Business

Contact Information for Business Card

Include agent name, contact info, website on front, licensing info for agent an company. Logo and services offered on back

Font styles to use
Other font styles liked:
• Avenir Next

Requirements
Must have
• See project description
Should not have
• Nothing cheesy

```html
<!DOCTYPE html>
<html lang="en">
<head>
<meta charset="utf-8">
<title>Niall Hargrove – Business Card</title>
<link rel="stylesheet" href="https://fonts.googleapis.com/css2?family=Nunito+Sans:wght@400;500&display=swap">
<style>
  :root {
    --dark-gray: #2c3539;
    --light-gray: #576870;
    --white: #ffffff;
    --stage: #737477;
    --ring: #555b5e;
  }
  * { margin: 0; padding: 0; box-sizing: border-box; }
  html, body { width: 1200px; height: 1200px; overflow: hidden; }
  body {
    background: var(--stage);
    font-family: "Nunito Sans", "Avenir Next", sans-serif;
    position: relative;
  }
  .card {
    position: absolute;
    width: 583px;
    height: 394px;
    background: var(--white);
    overflow: hidden;
  }
  .card-front { left: 305px; top: 138px; }
  .card-back  { left: 312px; top: 636px; }

  .brand-badge {
    position: absolute;
    width: 134px;
    height: 134px;
    border: 1px solid var(--ring);
    border-radius: 50%;
    display: flex;
    align-items: center;
    justify-content: center;
    text-align: center;
  }
  .brand-name {
    color: var(--light-gray);
    font-size: 14px;
    font-weight: 400;
    line-height: 1.3;
    width: 96px;
  }
  .card-front .brand-badge { left: 40px; top: 130px; }
  .card-back .brand-badge  { left: 225px; top: 130px; }

  .info-band {
    position: absolute;
    left: 192px;
    right: 0;
    color: var(--white);
    padding: 0 8px;
    display: flex;
    flex-direction: column;
    justify-content: center;
    font-size: 14px;
    line-height: 1.3;
    white-space: nowrap;
  }
  .band-dark  { background: var(--dark-gray); }
  .band-light { background: var(--light-gray); }
  .info-name    { top: 102px; height: 38px; font-size: 19px; }
  .info-address { top: 154px; height: 40px; }
  .info-phone   { top: 204px; height: 41px; }
  .info-license { top: 254px; height: 40px; }

  .services {
    position: absolute;
    left: 0;
    right: 0;
    top: 317px;
    height: 42px;
    display: flex;
    list-style: none;
  }
  .service {
    flex: 1;
    display: flex;
    align-items: center;
    justify-content: center;
    color: var(--white);
    font-size: 15px;
    background: var(--light-gray);
  }
  .service.band-dark { background: var(--dark-gray); }
</style>
</head>
<body>
  <section class="card card-front" aria-label="Card front">
    <div class="brand-badge"><span class="brand-name">The Hargrove Group</span></div>
    <div class="info-band band-dark info-name">Niall Hargrove | Loan Officer</div>
    <div class="info-band band-light info-address">
      <span>Keystone Lending | 880 Larkspur Avenue,</span>
      <span>Suite 210, San Jose, CA 95128</span>
    </div>
    <div class="info-band band-dark info-phone">
      <span>Phone 408-555-0172 x214 I Direct 650-555-0149</span>
      <span>Fax 408-555-0190</span>
    </div>
    <div class="info-band band-light info-license">
      <span>Fed and State License NMLS:482615</span>
      <span>DRE:02748163 CO:DRE:01937502/NMLS:576214</span>
    </div>
  </section>

  <section class="card card-back" aria-label="Card back">
    <div class="brand-badge"><span class="brand-name">The Hargrove Group</span></div>
    <ul class="services">
      <li class="service">Mortgage Loans</li>
      <li class="service band-dark">Reverse Mortgages</li>
      <li class="service">Private Money Loans</li>
    </ul>
  </section>
</body>
</html>
```